Brenway Productions photography and video creator

I need a business card for my production company. I shoot photography and videography for real estate, adventure sports and businesses

simple not to busy

Colors

Designer to choose colors to be used in the design.

Requirements
Must have
• dara@brenwayproductions.ca
• phone -5803317264
• instagram dara_brenway

```html
<!DOCTYPE html>
<html lang="en">
<head>
<meta charset="utf-8">
<title>Brenway Productions — Business Card</title>
<link href="https://fonts.googleapis.com/css2?family=Montserrat:wght@400;500&display=swap" rel="stylesheet">
<style>
  :root {
    --page-bg: #e9e5df;
    --card-dark: #3b3835;
    --card-light: #d9d1c4;
    --ring: #6f695f;
    --band: #8c8579;
    --text-light: #e6ddd0;
    --text-muted: #c9bfb1;
    --logo-fill: #2e2c2a;
    --logo-text: #e4d9c8;
  }
  * { margin: 0; padding: 0; box-sizing: border-box; }
  html, body {
    width: 1200px;
    height: 1047px;
    overflow: hidden;
    background: var(--page-bg);
    font-family: "Montserrat", sans-serif;
  }
  .card {
    position: absolute;
    left: 100px;
    top: 252px;
    width: 1000px;
    height: 542px;
    border-radius: 22px;
    overflow: hidden;
    box-shadow: 0 14px 40px rgba(40, 34, 28, 0.22);
  }
  .card-shapes { position: absolute; inset: 0; }
  .address {
    position: absolute;
    left: 40px;
    top: 70px;
    color: var(--text-muted);
    font-size: 24px;
    line-height: 34px;
    font-weight: 400;
  }
  .identity {
    position: absolute;
    left: 40px;
    top: 232px;
  }
  .identity-name {
    color: var(--text-light);
    font-size: 37px;
    font-weight: 500;
    letter-spacing: 2px;
    line-height: 44px;
  }
  .identity-role {
    color: var(--text-muted);
    font-size: 24px;
    letter-spacing: 1px;
    margin-top: 2px;
  }
  .contact {
    position: absolute;
    left: 40px;
    top: 394px;
    list-style: none;
    color: var(--text-muted);
    font-size: 24px;
  }
  .contact li {
    display: flex;
    align-items: center;
    height: 34.5px;
  }
  .contact-icon {
    width: 16px;
    height: 16px;
    margin-right: 10px;
    flex: none;
  }
  .brand-mark {
    position: absolute;
    left: 556px;
    top: 90px;
    width: 388px;
    height: 388px;
    border-radius: 50%;
    background: var(--logo-fill);
    display: flex;
    flex-direction: column;
    align-items: center;
    justify-content: center;
    color: var(--logo-text);
    font-weight: 500;
  }
  .brand-name {
    font-size: 50px;
    letter-spacing: 1px;
    line-height: 54px;
  }
  .brand-sub {
    font-size: 15px;
    letter-spacing: 6px;
    margin-top: 4px;
  }
</style>
</head>
<body>
  <div class="card">
    <svg class="card-shapes" width="1000" height="542" viewBox="0 0 1000 542">
      <defs>
        <mask id="dark-area">
          <rect width="1000" height="542" fill="#fff"/>
          <circle cx="750" cy="272" r="274" fill="#000"/>
        </mask>
      </defs>
      <rect class="light-face" width="1000" height="542" fill="var(--card-light)"/>
      <circle class="crescent-ring" cx="750" cy="272" r="274" fill="var(--ring)"/>
      <circle class="inner-face" cx="768" cy="280" r="262" fill="var(--card-light)"/>
      <g mask="url(#dark-area)">
        <rect class="dark-face" width="1000" height="542" fill="var(--card-dark)"/>
        <rect class="name-band" x="0" y="205" width="1000" height="131" fill="var(--band)"/>
      </g>
    </svg>

    <p class="address">217 Larkfield Avenue<br>Milbrook, PA 18420</p>

    <div class="identity">
      <p class="identity-name">DARA BRENWAY</p>
      <p class="identity-role">Managing Director</p>
    </div>

    <ul class="contact">
      <li>
        <svg class="contact-icon" viewBox="0 0 16 16"><path d="M3.5 1.5l2.4 2.8-1.4 1.8c.9 2 2.6 3.7 4.6 4.6l1.8-1.4 2.8 2.4-1.6 2.3C7.2 13.6 2.4 8.8 1.2 3.1z" fill="var(--text-muted)"/></svg>
        5803317264
      </li>
      <li>
        <svg class="contact-icon" viewBox="0 0 16 16"><rect x="1.5" y="3.5" width="13" height="9" rx="1" fill="none" stroke="var(--text-muted)" stroke-width="1.4"/><path d="M2 4l6 5 6-5" fill="none" stroke="var(--text-muted)" stroke-width="1.4"/></svg>
        dara@brenwayproductions.ca
      </li>
      <li>
        <svg class="contact-icon" viewBox="0 0 16 16"><rect x="2" y="2" width="12" height="12" fill="var(--text-muted)"/></svg>
        instagram dara_brenway
      </li>
    </ul>

    <div class="brand-mark">
      <span class="brand-name">BRENWAY</span>
      <span class="brand-sub">PRODUCTIONS</span>
    </div>
  </div>
</body>
</html>
```